International pain relief company needs flyer designed

We are based in South Australia, and are about to launch a brand new hand held portable fully chargeable pain relief device. This device gives the user proven instant relief often from the first time of use anywhere. We intend to offer, a try before you buy at home /office demonstration, a full 30 day money back guarantee and a full 3 year warranty. We also plan to give the first 7 people who book a demonstration a FREE $20 Norvane fuel card.
We are open minded regarding the overall design and colours used, however we are particularly keen on seeing pictures/cartoons of people suffering from the 3 main groups of pain, head ache, back ache and joint pain, perhaps also happy faces once they have been cured/relieved by our equipment. This product we expect to retail for around the $300 AUD mark.
The wording on the leaflet is
Suffering from headaches, back ache or joint problems?
At last....there is instant pain relief!
New to Australia, a personal portable pain relief device
Call Ted 0427586193 & 08 72514938
RWP Australia PO Box 618, Fernleigh SA 5094

Target Market(s)

aged, elderly

Industry/Entity Type

Retail

Font styles to use
Serif
Sans Serif

Colors
33b7a4
33a6d7
3176b5

Requirements
Must have
• include Free in house/office demonstration
Free $20 Norvan fuel card for first 11 demonstrations
Nice to have
• Norvane fuel logo

```html
<!DOCTYPE html>
<html lang="en">
<head>
<meta charset="utf-8">
<title>Portable Pain Relief Flyer</title>
<link rel="stylesheet" href="https://fonts.googleapis.com/css2?family=Marcellus+SC&family=Arimo:wght@400;700&display=swap">
<style>
  :root {
    --teal: #33b7a4;
    --teal-light: #9fdcd2;
    --teal-pale: #cdeee9;
    --sky: #33a6d7;
    --navy: #3176b5;
    --white: #ffffff;
    --photo-skin: #e6c9b8;
    --photo-grey: #b9b9b9;
    --pain-red: #e06a6a;
  }
  * { margin: 0; padding: 0; box-sizing: border-box; }
  html, body { width: 933px; height: 1200px; overflow: hidden; background: var(--white); }
  .flyer {
    position: relative; width: 933px; height: 1200px; overflow: hidden;
    background: var(--white);
    font-family: "Arimo", Arial, sans-serif; color: var(--white);
  }
  .main-panel {
    position: absolute; left: 0; top: 0; width: 755px; height: 960px;
    background: var(--teal);
  }
  .main-panel::before {
    content: ""; position: absolute; left: 0; top: 0; width: 324px; height: 960px;
    background: linear-gradient(180deg, var(--teal-light) 0%, rgba(51,183,164,0) 70%);
  }
  .side-stripe {
    position: absolute; left: 755px; width: 178px; height: 34px;
    background: linear-gradient(90deg, var(--teal-pale), rgba(205,238,233,0));
  }
  .side-stripe.upper { top: 276px; }
  .side-stripe.lower { top: 674px; }
  .photo {
    position: absolute; border-radius: 50%;
    border: 3px solid var(--teal);
    box-shadow: 0 0 0 4px var(--white);
  }
  .photo.wrist {
    left: 690px; top: 9px; width: 170px; height: 170px;
    background: radial-gradient(circle at 45% 45%, var(--pain-red) 0%, var(--photo-skin) 30%, var(--white) 80%);
  }
  .photo.headache {
    left: 654px; top: 351px; width: 202px; height: 202px;
    background: radial-gradient(circle at 55% 35%, var(--pain-red) 0%, var(--photo-skin) 28%, var(--photo-grey) 85%);
  }
  .photo.back {
    left: 580px; top: 755px; width: 202px; height: 202px;
    background: radial-gradient(circle at 60% 65%, var(--pain-red) 0%, var(--photo-skin) 30%, var(--white) 85%);
  }
  .headline {
    position: absolute; left: 0; top: 180px; width: 674px; text-align: center;
    font-family: "Marcellus SC", Georgia, serif; font-size: 31px; line-height: 42px;
    letter-spacing: 0.3px;
  }
  .intro {
    position: absolute; left: 0; top: 542px; width: 745px; text-align: center;
    font-weight: 700; font-size: 32px; line-height: 48px;
  }
  .offer {
    position: absolute; left: 0; top: 798px; width: 600px; text-align: center;
    font-size: 20px; line-height: 27px;
  }
  .fuel-brand {
    position: absolute; left: 33px; top: 868px; display: flex; align-items: center; gap: 8px;
    font-size: 18px; font-weight: 700;
  }
  .fuel-brand .dot { width: 46px; height: 46px; border-radius: 50%; background: var(--white); }
  .wave { position: absolute; left: 0; top: 920px; width: 933px; height: 120px; }
  .contact-band {
    position: absolute; left: 0; top: 1033px; width: 933px; height: 167px;
    background: linear-gradient(90deg, #e8f1f9 0%, var(--navy) 30%, var(--navy) 100%);
  }
  .contact-call {
    position: absolute; left: 0; top: 1032px; width: 898px; text-align: center;
    font-size: 30px;
  }
  .contact-phones {
    position: absolute; left: 0; top: 1072px; width: 898px; text-align: center;
    font-family: "Marcellus SC", Georgia, serif; font-size: 26px;
  }
  .contact-address {
    position: absolute; left: 51px; top: 1124px; font-size: 33px;
  }
</style>
</head>
<body>
<div class="flyer">
  <div class="main-panel"></div>
  <div class="side-stripe upper"></div>
  <div class="side-stripe lower"></div>

  <div class="photo wrist" role="img" aria-label="Photo of a hand holding a painful wrist"></div>
  <div class="photo headache" role="img" aria-label="Photo of a woman touching her temple with a headache"></div>
  <div class="photo back" role="img" aria-label="Photo of a person holding their aching lower back"></div>

  <h1 class="headline">Suffering from headaches,<br>back ache or<br>joint problems?<br>At last....there is instant pain relief!</h1>

  <p class="intro">New to Australia,<br>a personal portable pain relief device</p>

  <p class="offer">include Free in house/office demonstration<br>Free $20 Norvan fuel card for first 11 demonstrations</p>

  <div class="fuel-brand"><span class="dot"></span><span>Norvane</span></div>

  <svg class="wave" viewBox="0 0 933 120" preserveAspectRatio="none" aria-hidden="true">
    <path d="M0 20 C 250 -10, 600 40, 933 45 L933 120 L0 120 Z" fill="var(--sky)"/>
    <path d="M0 60 C 260 95, 620 75, 933 85 L933 120 L0 120 Z" fill="#e8f1f9"/>
  </svg>

  <div class="contact-band"></div>
  <p class="contact-call">Call Ted</p>
  <p class="contact-phones">0427586193 &amp; 08 72514938</p>
  <p class="contact-address">RWP Australia PO Box 618, Fernleigh SA 5094</p>
</div>
</body>
</html>
```